Harborline Portable Scans
Mobile Ultrasound
Every draft has been amazing. I didn't really understand that a small business card could be designed with so much artistry and imagination. Thanks to all who participated in this for us. Unfortunately, we can only pick one. I'm going to do that now. Thanks again to all! --Dale
THIS IS REALLY IMPORTANT!! Seems like I now have a new phone number! Please change the phone number on the card to 555.318.4426 on all drafts.
Thank You!
Thanks for all the FANTASTIC drafts! We've decided on a one sided card. Also, to my knowledge, all the logo formats should have been downloaded. I don't know how to upload an .ai file...I can contact someone at MarkSmith tomorrow to see if this can be done.
LOGO file has been uploaded!
--- Gerald
You wrote single-sided, but then wrote that you wanted your logo on the backside. Does that mean you want a double sided card? :)
Can you please upload an .ai file with the logo?

```html
<!DOCTYPE html>
<html lang="en">
<head>
<meta charset="utf-8">
<title>Harborline Portable Scans – Business Cards</title>
<link href="https://fonts.googleapis.com/css2?family=Arimo:wght@400;700&display=swap" rel="stylesheet">
<style>
  :root{
    --stage:#8c8c8e;
    --crimson:#a3141c;
    --crimson-deep:#7a0c12;
    --crimson-soft:#c9504a;
    --magenta:#b0124f;
    --ink:#1e1e1e;
    --cream-top:#fffdf0;
    --cream-bottom:#f5edc8;
    --silver-top:#ffffff;
    --silver-bottom:#c9c9cb;
    --white:#ffffff;
  }
  *{box-sizing:border-box;margin:0;padding:0}
  html,body{width:1200px;height:818px;overflow:hidden}
  body{background:var(--stage);font-family:"Arimo",Arial,sans-serif;color:var(--ink);position:relative}

  .card{position:absolute;border-radius:20px;overflow:hidden;box-shadow:3px 5px 10px rgba(0,0,0,.35)}
  .card--cream{left:36px;top:115px;width:576px;height:382px;
    background:linear-gradient(180deg,var(--cream-top),var(--cream-bottom))}
  .card--silver{left:630px;top:100px;width:540px;height:395px;
    background:linear-gradient(160deg,var(--silver-top) 30%,var(--silver-bottom))}
  .card--ultrasound{left:340px;top:500px;width:512px;height:302px;transform:rotate(2.5deg);
    background:linear-gradient(180deg,#fffde8,#f4eeb8)}

  .brand{position:absolute;display:flex;align-items:center;gap:12px;color:var(--magenta);
    font-weight:700;font-size:20px;line-height:1.15;letter-spacing:.5px;text-transform:uppercase}
  .brand__dot{width:34px;height:34px;border-radius:50%;background:var(--magenta);flex:none}

  .holder{position:absolute;white-space:nowrap}
  .holder__name{font-weight:700;font-size:17px}
  .holder__role{font-size:15px;margin-top:4px}

  .address{position:absolute;font-size:15px;line-height:1.25;letter-spacing:1.5px;white-space:nowrap}
  .online{position:absolute;color:var(--white);font-size:15px;line-height:1.3;letter-spacing:.5px;white-space:nowrap}

  .band{position:absolute;left:0;right:0;bottom:0;height:82px;
    background:linear-gradient(180deg,var(--crimson),var(--crimson-deep))}
  .band-edge{position:absolute;left:0;right:0;bottom:82px;height:10px;
    background:linear-gradient(90deg,var(--crimson-soft),#e7a48f)}

  .swoosh{position:absolute;left:0;bottom:0;width:540px;height:180px}

  .tagline{position:absolute;left:0;right:0;top:122px;height:30px;
    background:linear-gradient(90deg,#f0d9b0,var(--crimson) 25%,var(--crimson) 75%,#f0d9b0);
    color:var(--white);font-weight:700;font-size:17px;letter-spacing:4px;text-align:center;line-height:30px}
  .contact-small{position:absolute;font-size:10.5px;line-height:1.4;letter-spacing:0;white-space:nowrap}
</style>
</head>
<body>

<section class="card card--cream">
  <div class="brand" style="left:300px;top:48px;">
    <span class="brand__dot"></span><span>Harborline<br>Portable Scans</span>
  </div>
  <div class="holder" style="left:24px;top:162px;">
    <div class="holder__name">Dale Whitcomb, D.C.</div>
    <div class="holder__role">Executive Director</div>
  </div>
  <div class="address" style="left:322px;top:150px;">
    P.O. Box 212<br>Cedar Hollow, MI 49012<br>Ph.: 555.318.4426<br>Fax: 555.207.3391
  </div>
  <div class="band-edge"></div>
  <div class="band"></div>
  <div class="online" style="left:160px;top:310px;">
    e-mail: drwhitcomb@harborlineportablescans.com<br>web.: www.harborlineportablescans.com
  </div>
</section>

<section class="card card--silver">
  <svg class="swoosh" viewBox="0 0 540 180" preserveAspectRatio="none" aria-hidden="true">
    <defs>
      <linearGradient id="swooshFill" x1="0" y1="0" x2="0" y2="1">
        <stop offset="0" stop-color="#b31a20"/><stop offset="1" stop-color="#6e0a0f"/>
      </linearGradient>
    </defs>
    <path d="M0 20 C120 120 330 95 540 70 L540 180 L0 180 Z" fill="url(#swooshFill)"/>
    <path d="M0 20 C120 120 330 95 540 70" fill="none" stroke="#e8a0a0" stroke-width="3"/>
  </svg>
  <div class="holder" style="left:22px;top:30px;">
    <div class="holder__name">Dale Whitcomb, D.C.</div>
    <div class="holder__role">Executive Director</div>
  </div>
  <div class="brand" style="left:290px;top:50px;">
    <span class="brand__dot"></span><span>Harborline<br>Portable Scans</span>
  </div>
  <div class="address" style="left:318px;top:150px;">
    P.O. Box 212<br>Cedar Hollow, MI 49012<br>Ph.: 555.318.4426<br>Fax: 555.207.3391
  </div>
  <div class="online" style="left:70px;top:330px;">
    e-mail: drwhitcomb@harborlineportablescans.com<br>web.: www.harborlineportablescans.com
  </div>
</section>

<section class="card card--ultrasound">
  <div class="brand" style="left:150px;top:42px;">
    <span class="brand__dot"></span><span>Harborline<br>Portable Scans</span>
  </div>
  <div class="tagline">Mobile Ultrasound</div>
  <div class="holder" style="left:22px;top:178px;">
    <div class="holder__name">Dale Whitcomb, D.C.</div>
    <div class="holder__role">Executive Director</div>
  </div>
  <div class="contact-small" style="left:234px;top:172px;">
    P.O. Box 212, Cedar Hollow, MI 49012<br>Ph.: 555.318.4426, Fax: 555.207.3391<br>e-mail: drwhitcomb@harborlineportablescans.com<br>web.: www.harborlineportablescans.com
  </div>
</section>

</body>
</html>
```